Financial Services Company power point theme design

We need a PowerPoint theme designed for client presentations and company orientations. We do like modern designs using blue colors. attached is our logos the logo colors may change as needed to fit the theme. Landscape 16: 9 is acceptable

Industry/Entity Type

Financial Service

Colors

Designer to choose colors to be used in the design.

```html
<!DOCTYPE html>
<html lang="en">
<head>
<meta charset="utf-8">
<title>Keystone Ridge Financial – Presentation Theme</title>
<link rel="stylesheet" href="https://fonts.googleapis.com/css2?family=Oswald:wght@500;600&family=Lato:wght@400;700&family=Kaushan+Script&display=swap">
<style>
:root{
  --navy:#16305a;
  --ink:#0f1d36;
  --sky:#5aa6d6;
  --steel:#3d6f9c;
  --pale:#dce5f3;
  --paper:#f5f6f9;
  --facet:#e8ecf3;
  --teal:#1d6d85;
  --copy:#5b6170;
  --white:#ffffff;
}
html,body{margin:0;width:880px;height:1200px;overflow:hidden;background:var(--white)}
.canvas{position:relative;width:880px;height:1200px}
.slide{position:absolute;width:259px;height:145px;overflow:hidden;background:var(--paper);font-family:"Lato",sans-serif}
.slide.wide{width:388px;height:219px}
.abs{position:absolute}
.facets{position:absolute;inset:0;width:100%;height:100%}
.heading{font-family:"Oswald",sans-serif;font-weight:600;letter-spacing:.16em;color:var(--navy);font-size:10px;text-transform:uppercase;line-height:1;margin:0;white-space:nowrap}
.heading .accent{color:var(--sky)}
.heading-bar{position:absolute;height:4px;background:var(--sky)}
.rule{position:absolute;height:1.5px;background:var(--navy)}
.copy{font-size:4.2px;line-height:1.45;color:var(--copy);margin:0}
.copy.light{color:rgba(255,255,255,.78)}
.copy.center{text-align:center}
.copy.right{text-align:right}
.corner{position:absolute;width:30px;height:24px}
.corner.tl{left:0;top:0}
.corner.tr{right:0;top:0;transform:scaleX(-1)}
.corner.br{right:0;bottom:0;transform:rotate(180deg)}
.corner.bl{left:0;bottom:0;transform:scaleY(-1)}
.photo{position:absolute}
.photo.city{background:linear-gradient(135deg,#f2f3f5 0%,#b9bcc1 45%,#6d7178 75%,#a7aab0 100%)}
.photo.desk{background:linear-gradient(150deg,#3b3f45 0%,#6b5b4a 40%,#b08a64 70%,#d9d2c8 100%)}
.photo.work{background:linear-gradient(160deg,#e7e3dd 0%,#b7a791 50%,#6f5f4f 100%)}
.photo.portrait{background:linear-gradient(180deg,#7c8a8f 0%,#4a545a 50%,#2a2f35 100%)}
.photo.team{background:linear-gradient(180deg,#d9dde3 0%,#8e99a8 55%,#2f3f5c 100%)}
.photo.flatlay{background:linear-gradient(135deg,#5a4b3d 0%,#8a7663 50%,#3a3430 100%)}
.brand{font-family:"Lato",sans-serif;font-weight:700;color:var(--navy);text-transform:uppercase;letter-spacing:.06em;line-height:1.15;text-align:center;margin:0}
.brand-mark{display:block;background:var(--navy)}
.script{font-family:"Kaushan Script",cursive;color:var(--navy);margin:0;line-height:1}
.num{position:absolute;border-radius:50%;background:var(--ink);color:var(--white);font-family:"Oswald",sans-serif;font-weight:600;display:flex;align-items:center;justify-content:center}
.chart-title{font-family:"Lato",sans-serif;font-weight:700;font-size:3.6px;letter-spacing:.08em;fill:#555}
.cover-title{font-family:"Oswald",sans-serif;font-weight:600;text-transform:uppercase;letter-spacing:.06em;line-height:1.1;margin:0}
</style>
</head>
<body>
<svg width="0" height="0" style="position:absolute" aria-hidden="true">
  <defs>
    <symbol id="corner-shape" viewBox="0 0 30 24">
      <polygon points="0,0 30,0 0,24" fill="#16305a"/>
      <polygon points="0,0 14,0 0,11" fill="#2e5f8f"/>
    </symbol>
    <symbol id="pie" viewBox="0 0 40 40">
      <circle cx="20" cy="20" r="10" fill="none" stroke="#6fa3c7" stroke-width="20" pathLength="100" stroke-dasharray="58 100" transform="rotate(-40 20 20)"/>
      <circle cx="20" cy="20" r="10" fill="none" stroke="#0f1d36" stroke-width="20" pathLength="100" stroke-dasharray="22 100" stroke-dashoffset="-58" transform="rotate(-40 20 20)"/>
      <circle cx="20" cy="20" r="10" fill="none" stroke="#16305a" stroke-width="20" pathLength="100" stroke-dasharray="12 100" stroke-dashoffset="-80" transform="rotate(-40 20 20)"/>
      <circle cx="20" cy="20" r="10" fill="none" stroke="#5aa6d6" stroke-width="20" pathLength="100" stroke-dasharray="8 100" stroke-dashoffset="-92" transform="rotate(-40 20 20)"/>
    </symbol>
    <symbol id="facet-bg" viewBox="0 0 259 145" preserveAspectRatio="none">
      <polygon points="40,145 120,40 200,145" fill="#e8ecf3"/>
      <polygon points="150,0 259,0 259,90" fill="#edf0f6"/>
      <polygon points="0,60 60,145 0,145" fill="#e4e9f1"/>
    </symbol>
  </defs>
</svg>

<main class="canvas">

  <!-- Cover, diamond variant -->
  <section class="slide wide cover-diamond" style="left:45px;top:22px">
    <div class="photo city" style="inset:0" role="img" aria-label="Black and white photo looking up at a modern glass office building"></div>
    <svg class="abs" style="inset:0" width="388" height="219" aria-hidden="true">
      <polygon points="259,0 388,0 388,219 203,219" fill="#0f1d36"/>
      <polygon points="300,0 388,0 388,120" fill="#16305a" opacity=".55"/>
      <polygon points="60,219 110,219 40,150" fill="#16305a" opacity=".5"/>
    </svg>
    <div class="abs" style="left:57px;top:52px;width:118px;height:118px;transform:rotate(45deg);background:var(--pale);border:1.5px solid var(--navy);box-shadow:-5px 5px 0 0 var(--navy)"></div>
    <div class="abs" style="left:55px;top:88px;width:122px;text-align:center">
      <span class="brand-mark" style="width:12px;height:12px;margin:0 auto 5px"></span>
      <p class="brand" style="font-size:9px">Keystone Ridge<br>Financial LLC.</p>
    </div>
    <div class="abs" style="right:28px;top:88px;text-align:right">
      <p class="cover-title" style="font-size:20px;color:var(--white)">Your Title</p>
      <p class="cover-title" style="font-size:20px;color:var(--sky)">Text Here</p>
      <p style="margin:6px 0 0;font-size:10px;color:var(--white);letter-spacing:.03em">Subtitle text here</p>
    </div>
    <p class="copy right" style="position:absolute;right:22px;top:172px;width:110px;color:#3f6ea3">Lorem ipsum dolor sit amet, quem prompta forensibus ei has, has saepe eloquentiam at.</p>
  </section>

  <!-- Cover, split variant -->
  <section class="slide wide cover-split" style="left:449px;top:22px">
    <div class="photo city" style="left:176px;top:0;width:212px;height:219px;background:linear-gradient(160deg,#fafafa 0%,#d9dbdf 55%,#8e9298 100%)" role="img" aria-label="Light photo of a glass office tower"></div>
    <svg class="abs" style="left:0;top:0" width="176" height="219" aria-hidden="true">
      <rect width="176" height="219" fill="#0f1d36"/>
      <polygon points="0,140 120,219 0,219" fill="#16305a" opacity=".6"/>
    </svg>
    <div class="abs" style="right:234px;top:32px;text-align:right">
      <p class="cover-title" style="font-size:20px;color:var(--white)">Your Title</p>
      <p class="cover-title" style="font-size:20px;color:var(--sky)">Text Here</p>
      <p style="margin:6px 0 0;font-size:10px;color:var(--white);letter-spacing:.03em">Subtitle text here</p>
    </div>
    <p class="copy center" style="position:absolute;left:36px;top:168px;width:120px;color:#3f6ea3">Lorem ipsum dolor sit amet, quem prompta forensibus ei has, has saepe eloquentiam at.</p>
    <div class="abs" style="left:214px;top:54px;width:134px;text-align:center">
      <span class="brand-mark" style="width:16px;height:16px;margin:0 auto 6px"></span>
      <p class="brand" style="font-size:11px">Keystone Ridge<br>Financial LLC.</p>
    </div>
    <div class="abs" style="left:206px;top:146px;width:44px;text-align:center">
      <span class="brand-mark" style="width:7px;height:7px;margin:0 auto 3px"></span>
      <p class="brand" style="font-size:4px">Home<br>Lending</p>
    </div>
    <div class="abs" style="left:258px;top:146px;width:44px;text-align:center">
      <span class="brand-mark" style="width:7px;height:7px;margin:0 auto 3px"></span>
      <p class="brand" style="font-size:4px">Insurance<br>Group</p>
    </div>
    <div class="abs" style="left:310px;top:146px;width:50px;text-align:center">
      <span class="brand-mark" style="width:7px;height:7px;margin:0 auto 3px"></span>
      <p class="brand" style="font-size:4px">Keystone Ridge<br>Financial LLC.</p>
    </div>
  </section>

  <!-- About us -->
  <section class="slide about" style="left:45px;top:257px">
    <svg class="facets" aria-hidden="true"><use href="#facet-bg"/></svg>
    <svg class="corner tl" aria-hidden="true"><use href="#corner-shape"/></svg>
    <div class="heading-bar" style="left:74px;top:19px;width:12px"></div>
    <h2 class="heading abs" style="left:90px;top:16px">About Us</h2>
    <p class="copy abs" style="left:17px;top:42px;width:120px">Lorem ipsum dolor sit amet, quem prompta forensibus ei has, has saepe eloquentiam at. Enim consulatu percipitur ut nec, est fugit iudicabit te, alia consulatu an ius. Ea est numquam ancillae mediocritatem, habemus recteque no ius, mei eu possit conceptam.</p>
    <p class="copy abs" style="left:17px;top:84px;width:120px">In mea eque viderer detracto. Erant libris in cum, dolorum fabellas ei nec. Dolore mucius lucilius vix an, vim perpetua dissentias temporibus ut, partem recteque sea eu. Ne sed quas tantas noster tincidunt an vix. Sed dicunt dignissim honestatis te, velit omnis falli at has.</p>
    <div class="abs" style="left:188px;top:20px;width:58px;text-align:center">
      <span class="brand-mark" style="width:8px;height:8px;margin:0 auto 3px"></span>
      <p class="brand" style="font-size:4.6px">Keystone Ridge<br>Financial LLC.</p>
    </div>
    <div class="abs" style="left:157px;top:65px;width:92px;height:66px;background:var(--navy)"></div>
    <div class="photo desk" style="left:151px;top:59px;width:92px;height:66px" role="img" aria-label="Photo of a laptop and headphones on a desk"></div>
  </section>

  <!-- Meet our team -->
  <section class="slide team" style="left:311px;top:257px">
    <svg class="facets" aria-hidden="true"><use href="#facet-bg"/></svg>
    <h2 class="heading abs" style="left:88px;top:16px"><span class="accent">Meet</span> Our Team</h2>
    <div class="heading-bar" style="left:180px;top:19px;width:12px"></div>
    <div class="photo team" style="left:29px;top:38px;width:46px;height:46px" role="img" aria-label="Portrait photo of a team member"></div>
    <div class="photo team" style="left:106px;top:38px;width:46px;height:46px" role="img" aria-label="Portrait photo of a team member"></div>
    <div class="photo team" style="left:186px;top:38px;width:46px;height:46px" role="img" aria-label="Portrait photo of a team member"></div>
    <svg class="abs" style="left:0;top:0" width="259" height="145" aria-hidden="true" fill="#16305a">
      <rect x="24" y="59" width="4" height="4" transform="rotate(45 26 61)"/>
      <rect x="76" y="59" width="4" height="4" transform="rotate(45 78 61)"/>
      <rect x="101" y="59" width="4" height="4" transform="rotate(45 103 61)"/>
      <rect x="153" y="59" width="4" height="4" transform="rotate(45 155 61)"/>
      <rect x="181" y="59" width="4" height="4" transform="rotate(45 183 61)"/>
      <rect x="233" y="59" width="4" height="4" transform="rotate(45 235 61)"/>
      <rect x="50" y="34" width="4" height="4" transform="rotate(45 52 36)"/>
      <rect x="127" y="34" width="4" height="4" transform="rotate(45 129 36)"/>
      <rect x="207" y="34" width="4" height="4" transform="rotate(45 209 36)"/>
    </svg>
    <p class="script abs" style="left:26px;top:88px;width:52px;text-align:center;font-size:5px">Full Name</p>
    <p class="script abs" style="left:103px;top:88px;width:52px;text-align:center;font-size:5px">Full Name</p>
    <p class="script abs" style="left:183px;top:88px;width:52px;text-align:center;font-size:5px">Full Name</p>
    <p class="copy center abs" style="left:26px;top:95px;width:52px">Lorem ipsum dolor sit amet, quem prompta forensibus ei has, has saepe eloquentiam at.</p>
    <p class="copy center abs" style="left:103px;top:95px;width:52px">Lorem ipsum dolor sit amet, quem prompta forensibus ei has, has saepe eloquentiam at.</p>
    <p class="copy center abs" style="left:183px;top:95px;width:52px">Lorem ipsum dolor sit amet, quem prompta forensibus ei has, has saepe eloquentiam at.</p>
  </section>

  <!-- Our profile -->
  <section class="slide profile" style="left:578px;top:257px">
    <svg class="facets" aria-hidden="true"><use href="#facet-bg"/></svg>
    <h2 class="heading abs" style="left:45px;top:20px">Our Profile</h2>
    <div class="heading-bar" style="left:118px;top:23px;width:12px"></div>
    <p class="script abs" style="left:40px;top:55px;width:100px;text-align:center;font-size:11px">Name <span style="color:var(--sky)">Here</span></p>
    <p class="copy center abs" style="left:28px;top:76px;width:114px">Lorem ipsum dolor sit amet, quem prompta forensibus ei has, has saepe eloquentiam at. Enim consulatu percipitur ut nec, est fugit iudicabit te, alia consulatu an ius. Eu est numquam ancillae mediocritatem, habemus recteque no ius, mei eu possit conceptam. Pro id idque omittam, his ei quas phaedrum quaerendum.</p>
    <div class="photo portrait" style="left:144px;top:0;width:115px;height:145px" role="img" aria-label="Portrait photo of a professional in an office"></div>
  </section>

  <!-- Contents -->
  <section class="slide contents" style="left:45px;top:413px">
    <svg class="facets" aria-hidden="true"><use href="#facet-bg"/></svg>
    <svg class="corner tl" aria-hidden="true"><use href="#corner-shape"/></svg>
    <div class="heading-bar" style="left:88px;top:24px;width:12px"></div>
    <h2 class="heading abs" style="left:104px;top:21px">Contents</h2>
    <div class="num" style="left:24px;top:53px;width:10px;height:10px;font-size:5px">1</div>
    <div class="num" style="left:24px;top:83px;width:10px;height:10px;font-size:5px">2</div>
    <div class="num" style="left:24px;top:113px;width:10px;height:10px;font-size:5px">3</div>
    <div class="num" style="left:144px;top:53px;width:10px;height:10px;font-size:5px">4</div>
    <div class="num" style="left:144px;top:83px;width:10px;height:10px;font-size:5px">5</div>
    <div class="num" style="left:144px;top:113px;width:10px;height:10px;font-size:5px">6</div>
    <div class="abs" style="left:45px;top:53px;font-size:4.6px;color:var(--ink)"><b style="font-weight:700">Lorem ipsum</b><br><span style="color:var(--copy)">Lorem ipsum dolor sit amet</span></div>
    <div class="abs" style="left:45px;top:83px;font-size:4.6px;color:var(--ink)"><b>Lorem ipsum</b><br><span style="color:var(--copy)">Lorem ipsum dolor sit amet</span></div>
    <div class="abs" style="left:45px;top:113px;font-size:4.6px;color:var(--ink)"><b>Lorem ipsum</b><br><span style="color:var(--copy)">Lorem ipsum dolor sit amet</span></div>
    <div class="abs" style="left:165px;top:53px;font-size:4.6px;color:var(--ink)"><b>Lorem ipsum</b><br><span style="color:var(--copy)">Lorem ipsum dolor sit amet</span></div>
    <div class="abs" style="left:165px;top:83px;font-size:4.6px;color:var(--ink)"><b>Lorem ipsum</b><br><span style="color:var(--copy)">Lorem ipsum dolor sit amet</span></div>
    <div class="abs" style="left:165px;top:113px;font-size:4.6px;color:var(--ink)"><b>Lorem ipsum</b><br><span style="color:var(--copy)">Lorem ipsum dolor sit amet</span></div>
  </section>

  <!-- Left picture slide -->
  <section class="slide picture-left" style="left:311px;top:413px">
    <svg class="facets" aria-hidden="true"><use href="#facet-bg"/></svg>
    <div class="abs" style="left:0;top:0;width:124px;height:145px;background:var(--pale)"></div>
    <div class="photo desk" style="left:18px;top:17px;width:111px;height:112px" role="img" aria-label="Photo of hands typing on a laptop at a wooden desk"></div>
    <svg class="corner tr" aria-hidden="true"><use href="#corner-shape"/></svg>
    <h2 class="heading abs" style="left:140px;top:26px;font-size:13px">Left</h2>
    <h3 class="heading abs" style="left:140px;top:45px;font-size:7px">Picture Slide</h3>
    <div class="rule" style="left:160px;top:57px;width:36px"></div>
    <p class="copy right abs" style="left:172px;top:90px;width:72px">Lorem ipsum dolor sit amet, quem prompta forensibus ei has, has saepe eloquentiam at. Enim consulatu percipitur ut nec, est fugit iudicabit te, alia consulatu an ius. Eu est numquam ancillae mediocritatem, habemus recteque no ius, mei eu possit conceptam.</p>
  </section>

  <!-- Right picture slide -->
  <section class="slide picture-right" style="left:578px;top:413px">
    <svg class="facets" aria-hidden="true"><use href="#facet-bg"/></svg>
    <div class="abs" style="left:142px;top:0;width:117px;height:145px;background:var(--pale)"></div>
    <div class="photo desk" style="left:124px;top:17px;width:111px;height:112px" role="img" aria-label="Photo of hands typing on a laptop at a wooden desk"></div>
    <svg class="corner tl" aria-hidden="true"><use href="#corner-shape"/></svg>
    <h2 class="heading abs" style="right:162px;top:26px;font-size:13px">Right</h2>
    <h3 class="heading abs" style="right:162px;top:45px;font-size:7px">Picture Slide</h3>
    <div class="rule" style="left:62px;top:57px;width:36px"></div>
    <p class="copy right abs" style="left:40px;top:90px;width:74px">Lorem ipsum dolor sit amet, quem prompta forensibus ei has, has saepe eloquentiam at. Enim consulatu percipitur ut nec, est fugit iudicabit te, alia consulatu an ius. Eu est numquam ancillae mediocritatem, habemus recteque no ius, mei eu possit conceptam.</p>
  </section>

  <!-- Full picture slide -->
  <section class="slide picture-full" style="left:45px;top:567px">
    <div class="photo desk" style="inset:0;background:linear-gradient(160deg,#9aa3ad 0%,#cfd4da 45%,#e6e8eb 100%)" role="img" aria-label="Soft background photo of hands typing on a laptop with glasses beside it"></div>
    <div class="abs" style="inset:0;background:rgba(255,255,255,.45)"></div>
    <h2 class="heading abs" style="left:0;width:259px;text-align:center;top:24px;font-size:13px">Full</h2>
    <h3 class="heading abs" style="left:0;width:259px;text-align:center;top:43px;font-size:7px">Picture Slide</h3>
    <div class="rule" style="left:111px;top:55px;width:36px"></div>
    <p class="copy center abs" style="left:82px;top:76px;width:94px;color:#3f4552">Lorem ipsum dolor sit amet, quem prompta forensibus ei has, has saepe eloquentiam at. Enim consulatu percipitur ut nec, est fugit iudicabit te, alia consulatu an ius. Eu est numquam ancillae mediocritatem, habemus recteque no ius, mei eu possit conceptam.</p>
  </section>

  <!-- Two picture slide -->
  <section class="slide picture-two" style="left:311px;top:567px">
    <svg class="facets" aria-hidden="true"><use href="#facet-bg"/></svg>
    <div class="abs" style="left:0;top:0;width:117px;height:145px;background:var(--pale)"></div>
    <div class="photo flatlay" style="left:18px;top:18px;width:85px;height:66px" role="img" aria-label="Top-down photo of a notebook, pens and coffee on a dark desk"></div>
    <div class="photo work" style="left:38px;top:63px;width:96px;height:64px;box-shadow:0 0 0 1.5px var(--white)" role="img" aria-label="Top-down photo of a laptop and papers on a wooden table"></div>
    <svg class="corner tr" aria-hidden="true"><use href="#corner-shape"/></svg>
    <h2 class="heading abs" style="left:137px;top:24px;font-size:13px">Two</h2>
    <h3 class="heading abs" style="left:137px;top:43px;font-size:7px">Picture Slide</h3>
    <div class="rule" style="left:158px;top:55px;width:36px"></div>
    <p class="copy right abs" style="left:170px;top:88px;width:74px">Lorem ipsum dolor sit amet, quem prompta forensibus ei has, has saepe eloquentiam at. Enim consulatu percipitur ut nec, est fugit iudicabit te, alia consulatu an ius. Eu est numquam ancillae mediocritatem, habemus recteque no ius, mei eu possit conceptam.</p>
  </section>

  <!-- Three picture slide -->
  <section class="slide picture-three" style="left:578px;top:567px">
    <svg class="facets" aria-hidden="true"><use href="#facet-bg"/></svg>
    <svg class="corner tr" aria-hidden="true"><use href="#corner-shape"/></svg>
    <svg class="corner bl" aria-hidden="true"><use href="#corner-shape"/></svg>
    <h2 class="heading abs" style="left:0;width:259px;text-align:center;top:12px;font-size:13px;color:var(--sky)">Three</h2>
    <h3 class="heading abs" style="left:0;width:259px;text-align:center;top:30px;font-size:8px">Picture Slide</h3>
    <p class="copy center abs" style="left:30px;top:44px;width:199px">Lorem ipsum dolor sit amet, eu his iudico pertinax intellegebat, sensurit postulant mnesarchum ut eos.</p>
    <div class="photo work" style="left:36px;top:62px;width:40px;height:38px" role="img" aria-label="Photo of a person writing in a notebook"></div>
    <div class="photo work" style="left:110px;top:62px;width:40px;height:38px" role="img" aria-label="Photo of a person working at a laptop"></div>
    <div class="photo work" style="left:183px;top:62px;width:40px;height:38px" role="img" aria-label="Photo of documents and a pen on a desk"></div>
    <p class="copy center abs" style="left:30px;top:104px;width:52px">Lorem ipsum dolor sit amet, quem prompta forensibus ei has, has saepe eloquentiam at.</p>
    <p class="copy center abs" style="left:104px;top:104px;width:52px">Lorem ipsum dolor sit amet, quem prompta forensibus ei has, has saepe eloquentiam at.</p>
    <p class="copy center abs" style="left:177px;top:104px;width:52px">Lorem ipsum dolor sit amet, quem prompta forensibus ei has, has saepe eloquentiam at.</p>
  </section>

  <!-- List slide: steps -->
  <section class="slide list-steps" style="left:45px;top:722px">
    <svg class="facets" aria-hidden="true"><use href="#facet-bg"/></svg>
    <svg class="corner tl" aria-hidden="true"><use href="#corner-shape"/></svg>
    <svg class="corner br" aria-hidden="true"><use href="#corner-shape"/></svg>
    <div class="heading-bar" style="left:88px;top:22px;width:12px"></div>
    <h2 class="heading abs" style="left:104px;top:19px">List Slide</h2>
    <div class="num" style="left:47px;top:48px;width:20px;height:20px;font-size:11px">1</div>
    <div class="num" style="left:121px;top:48px;width:20px;height:20px;font-size:11px">2</div>
    <div class="num" style="left:192px;top:48px;width:20px;height:20px;font-size:11px">3</div>
    <svg class="abs" style="left:0;top:0" width="259" height="145" aria-hidden="true" fill="none" stroke="#16305a" stroke-width=".8">
      <polyline points="92,54 99,70 92,86"/>
      <polyline points="163,54 170,70 163,86"/>
    </svg>
    <p class="abs" style="left:29px;top:76px;width:56px;margin:0;text-align:center;font-size:4.6px;font-weight:700;color:var(--ink)">Title Here</p>
    <p class="abs" style="left:103px;top:76px;width:56px;margin:0;text-align:center;font-size:4.6px;font-weight:700;color:var(--ink)">Title Here</p>
    <p class="abs" style="left:174px;top:76px;width:56px;margin:0;text-align:center;font-size:4.6px;font-weight:700;color:var(--ink)">Title Here</p>
    <p class="copy center abs" style="left:29px;top:84px;width:56px">Lorem ipsum dolor sit amet, quem prompta forensibus ei has, has saepe eloquentiam at. Enim consulatu percipitur ut nec, est fugit iudicabit te.</p>
    <p class="copy center abs" style="left:103px;top:84px;width:56px">Lorem ipsum dolor sit amet, quem prompta forensibus ei has, has saepe eloquentiam at. Enim consulatu percipitur ut nec, est fugit iudicabit te.</p>
    <p class="copy center abs" style="left:174px;top:84px;width:56px">Lorem ipsum dolor sit amet, quem prompta forensibus ei has, has saepe eloquentiam at. Enim consulatu percipitur ut nec, est fugit iudicabit te.</p>
  </section>

  <!-- List slide: cards -->
  <section class="slide list-cards" style="left:311px;top:722px">
    <svg class="facets" aria-hidden="true"><use href="#facet-bg"/></svg>
    <svg class="corner tl" aria-hidden="true"><use href="#corner-shape"/></svg>
    <svg class="corner tr" aria-hidden="true"><use href="#corner-shape"/></svg>
    <div class="heading-bar" style="left:88px;top:22px;width:12px"></div>
    <h2 class="heading abs" style="left:104px;top:19px">List Slide</h2>
    <div class="abs" style="left:29px;top:48px;width:54px;height:82px;background:var(--ink)"></div>
    <div class="abs" style="left:101px;top:48px;width:54px;height:82px;background:var(--ink)"></div>
    <div class="abs" style="left:174px;top:48px;width:54px;height:82px;background:var(--ink)"></div>
    <div class="num" style="left:47px;top:55px;width:18px;height:18px;font-size:10px;background:var(--white);color:var(--ink)">1</div>
    <div class="num" style="left:119px;top:55px;width:18px;height:18px;font-size:10px;background:var(--white);color:var(--ink)">2</div>
    <div class="num" style="left:192px;top:55px;width:18px;height:18px;font-size:10px;background:var(--white);color:var(--ink)">3</div>
    <p class="copy center light abs" style="left:33px;top:80px;width:46px">Lorem ipsum dolor sit amet, quem prompta forensibus ei has, has saepe eloquentiam at. Enim consulatu percipitur ut nec, est fugit iudicabit te.</p>
    <p class="copy center light abs" style="left:105px;top:80px;width:46px">Lorem ipsum dolor sit amet, quem prompta forensibus ei has, has saepe eloquentiam at. Enim consulatu percipitur ut nec, est fugit iudicabit te.</p>
    <p class="copy center light abs" style="left:178px;top:80px;width:46px">Lorem ipsum dolor sit amet, quem prompta forensibus ei has, has saepe eloquentiam at. Enim consulatu percipitur ut nec, est fugit iudicabit te.</p>
  </section>

  <!-- List slide: grid -->
  <section class="slide list-grid" style="left:578px;top:722px">
    <svg class="facets" aria-hidden="true"><use href="#facet-bg"/></svg>
    <svg class="corner tl" aria-hidden="true"><use href="#corner-shape"/></svg>
    <svg class="corner tr" aria-hidden="true"><use href="#corner-shape"/></svg>
    <h2 class="heading abs" style="left:98px;top:19px">List Slide</h2>
    <div class="heading-bar" style="left:160px;top:22px;width:18px"></div>
    <div class="abs" style="left:22px;top:50px;width:56px;height:23px;padding:5px;background:var(--pale)"><p class="copy center">Lorem ipsum dolor sit amet, quem prompta forensibus ei has, has saepe eloquentiam at.</p></div>
    <div class="abs" style="left:97px;top:50px;width:56px;height:23px;padding:5px;background:var(--ink)"><p class="copy center light">Lorem ipsum dolor sit amet, quem prompta forensibus ei has, has saepe eloquentiam at.</p></div>
    <div class="abs" style="left:172px;top:50px;width:56px;height:23px;padding:5px;background:var(--pale)"><p class="copy center">Lorem ipsum dolor sit amet, quem prompta forensibus ei has, has saepe eloquentiam at.</p></div>
    <div class="abs" style="left:22px;top:94px;width:56px;height:23px;padding:5px;background:var(--ink)"><p class="copy center light">Lorem ipsum dolor sit amet, quem prompta forensibus ei has, has saepe eloquentiam at.</p></div>
    <div class="abs" style="left:97px;top:94px;width:56px;height:23px;padding:5px;background:var(--pale)"><p class="copy center">Lorem ipsum dolor sit amet, quem prompta forensibus ei has, has saepe eloquentiam at.</p></div>
    <div class="abs" style="left:172px;top:94px;width:56px;height:23px;padding:5px;background:var(--ink)"><p class="copy center light">Lorem ipsum dolor sit amet, quem prompta forensibus ei has, has saepe eloquentiam at.</p></div>
  </section>

  <!-- Data slide: three pies -->
  <section class="slide data-pies" style="left:45px;top:877px">
    <svg class="facets" aria-hidden="true"><use href="#facet-bg"/></svg>
    <svg class="corner tr" aria-hidden="true"><use href="#corner-shape"/></svg>
    <h2 class="heading abs" style="left:13px;top:19px">Data Slide</h2>
    <div class="rule" style="left:13px;top:33px;width:68px"></div>
    <p class="copy abs" style="left:13px;top:38px;width:220px">Lorem ipsum dolor sit amet, quem prompta forensibus ei has, has saepe eloquentiam at. Enim consulatu percipitur ut nec, est fugit iudicabit te, alia consulatu an ius.</p>
    <svg class="abs" style="left:0;top:0" width="259" height="145" aria-label="Three pie charts of sales for three years" role="img">
      <text x="50" y="89" class="chart-title" font-size="3px">SALES 2015</text>
      <text x="128" y="74" class="chart-title" font-size="3px">SALES 2017</text>
      <text x="218" y="66" class="chart-title" font-size="3px">SALES 2019</text>
      <use href="#pie" x="26" y="90" width="32" height="32"/>
      <use href="#pie" x="99" y="73" width="44" height="44"/>
      <use href="#pie" x="179" y="64" width="54" height="54"/>
      <g font-size="2.6" fill="#777" font-family="Lato, sans-serif">
        <circle cx="22" cy="134" r="1" fill="#6fa3c7"/><text x="24" y="135">1st Qtr</text>
        <circle cx="34" cy="134" r="1" fill="#0f1d36"/><text x="36" y="135">2nd Qtr</text>
        <circle cx="47" cy="134" r="1" fill="#16305a"/><text x="49" y="135">3rd Qtr</text>
        <circle cx="59" cy="134" r="1" fill="#5aa6d6"/><text x="61" y="135">4th Qtr</text>
        <circle cx="100" cy="134" r="1" fill="#6fa3c7"/><text x="102" y="135">1st Qtr</text>
        <circle cx="112" cy="134" r="1" fill="#0f1d36"/><text x="114" y="135">2nd Qtr</text>
        <circle cx="125" cy="134" r="1" fill="#16305a"/><text x="127" y="135">3rd Qtr</text>
        <circle cx="137" cy="134" r="1" fill="#5aa6d6"/><text x="139" y="135">4th Qtr</text>
        <circle cx="185" cy="134" r="1" fill="#6fa3c7"/><text x="187" y="135">1st Qtr</text>
        <circle cx="197" cy="134" r="1" fill="#0f1d36"/><text x="199" y="135">2nd Qtr</text>
        <circle cx="210" cy="134" r="1" fill="#16305a"/><text x="212" y="135">3rd Qtr</text>
        <circle cx="222" cy="134" r="1" fill="#5aa6d6"/><text x="224" y="135">4th Qtr</text>
      </g>
    </svg>
  </section>

  <!-- Data slide: table and line chart -->
  <section class="slide data-table" style="left:311px;top:877px">
    <svg class="facets" aria-hidden="true"><use href="#facet-bg"/></svg>
    <svg class="corner tl" aria-hidden="true"><use href="#corner-shape"/></svg>
    <svg class="corner br" aria-hidden="true"><use href="#corner-shape"/></svg>
    <h2 class="heading abs" style="left:0;width:259px;text-align:center;top:14px">Data Slide</h2>
    <div class="rule" style="left:111px;top:28px;width:36px"></div>
    <p class="copy center abs" style="left:30px;top:34px;width:199px">Lorem ipsum dolor sit amet, eu his iudico pertinax intellegebat, sensurit postulant mnesarchum ut eos.</p>
    <svg class="abs" style="left:0;top:0" width="259" height="145" role="img" aria-label="Data table beside a line chart with three series">
      <g font-family="Lato, sans-serif" font-size="3.2">
        <rect x="26" y="59" width="108" height="7" fill="#0f1d36"/>
        <g fill="#fff" font-weight="700"><text x="28" y="64">No</text><text x="46" y="64">Lorem</text><text x="78" y="64">Ipsum</text><text x="108" y="64">Dolor</text></g>
        <rect x="26" y="66" width="108" height="6" fill="#e3e9f3"/>
        <rect x="26" y="72" width="108" height="6" fill="#ffffff"/>
        <rect x="26" y="78" width="108" height="6" fill="#e3e9f3"/>
        <rect x="26" y="84" width="108" height="6" fill="#ffffff"/>
        <g fill="#555">
          <text x="28" y="70.5">1</text><text x="46" y="70.5">Stuff</text><text x="78" y="70.5">Thing</text><text x="108" y="70.5">Amount</text>
          <text x="28" y="76.5">2</text><text x="46" y="76.5">Stuff</text><text x="78" y="76.5">Thing</text><text x="108" y="76.5">Amount</text>
          <text x="28" y="82.5">3</text><text x="46" y="82.5">Stuff</text><text x="78" y="82.5">Thing</text><text x="108" y="82.5">Amount</text>
          <text x="28" y="88.5">4</text><text x="46" y="88.5">Stuff</text><text x="78" y="88.5">Thing</text><text x="108" y="88.5">Amount</text>
        </g>
      </g>
      <text x="179" y="56" class="chart-title" font-size="3px">CHART TITLE</text>
      <g stroke="#dfe3ea" stroke-width=".3"><line x1="155" y1="65" x2="235" y2="65"/><line x1="155" y1="73" x2="235" y2="73"/><line x1="155" y1="81" x2="235" y2="81"/><line x1="155" y1="89" x2="235" y2="89"/><line x1="155" y1="97" x2="235" y2="97"/></g>
      <polyline points="160,88 178,78 196,84 214,74 232,70" fill="none" stroke="#16305a" stroke-width=".7"/>
      <polyline points="160,80 178,86 196,76 214,82 232,74" fill="none" stroke="#0f1d36" stroke-width=".7"/>
      <polyline points="160,92 178,84 196,88 214,80 232,66" fill="none" stroke="#5aa6d6" stroke-width=".7"/>
    </svg>
    <p class="copy center abs" style="left:30px;top:115px;width:199px">Lorem ipsum dolor sit amet, quem prompta forensibus ei has, has saepe eloquentiam at. Enim consulatu percipitur ut nec, est fugit iudicabit te, alia consulatu an ius.</p>
  </section>

  <!-- Data slide: line chart with side panel -->
  <section class="slide data-line" style="left:578px;top:877px">
    <svg class="facets" aria-hidden="true"><use href="#facet-bg"/></svg>
    <h2 class="heading abs" style="left:17px;top:18px">Data Slide</h2>
    <div class="rule" style="left:17px;top:32px;width:36px"></div>
    <p class="copy abs" style="left:17px;top:38px;width:128px">Lorem ipsum dolor sit amet, quem prompta forensibus ei has, has saepe eloquentiam at. Enim consulatu percipitur ut nec, est fugit iudicabit te, alia consulatu an ius.</p>
    <svg class="abs" style="left:0;top:0" width="259" height="145" role="img" aria-label="Line chart with three series across four categories">
      <text x="68" y="67" class="chart-title" font-size="3px">CHART TITLE</text>
      <g stroke="#dfe3ea" stroke-width=".3"><line x1="24" y1="80" x2="132" y2="80"/><line x1="24" y1="92" x2="132" y2="92"/><line x1="24" y1="104" x2="132" y2="104"/><line x1="24" y1="116" x2="132" y2="116"/><line x1="24" y1="128" x2="132" y2="128"/></g>
      <polyline points="30,100 58,118 86,104 114,112 128,100" fill="none" stroke="#16305a" stroke-width=".7"/>
      <polyline points="30,114 58,102 86,116 114,100 128,96" fill="none" stroke="#0f1d36" stroke-width=".7"/>
      <polyline points="30,120 58,112 86,108 114,96 128,86" fill="none" stroke="#5aa6d6" stroke-width=".7"/>
      <g font-size="2.4" fill="#888" font-family="Lato, sans-serif"><text x="24" y="134">CATEGORY 1</text><text x="52" y="134">CATEGORY 2</text><text x="80" y="134">CATEGORY 3</text><text x="108" y="134">CATEGORY 4</text></g>
    </svg>
    <div class="abs" style="left:157px;top:0;width:102px;height:145px;background:var(--ink)"></div>
    <p class="copy light abs" style="left:166px;top:12px;width:84px;text-align:justify">Lorem ipsum dolor sit amet, quem prompta forensibus ei has, has saepe eloquentiam at. Enim consulatu percipitur ut nec, est fugit iudicabit te, alia consulatu an ius.</p>
    <p class="copy light abs" style="left:166px;top:58px;width:84px;text-align:justify">Lorem ipsum dolor sit amet, quem prompta forensibus ei has, has saepe eloquentiam at. Enim consulatu percipitur ut nec, est fugit iudicabit te, alia consulatu an ius.</p>
  </section>

  <!-- Data slide: bar chart with side panel -->
  <section class="slide data-bars" style="left:45px;top:1032px">
    <svg class="facets" aria-hidden="true"><use href="#facet-bg"/></svg>
    <div class="photo" style="left:0;top:0;width:102px;height:145px;background:linear-gradient(160deg,#26334a 0%,#162238 55%,#0d1628 100%)" role="img" aria-label="Dark navy-tinted photo of an office workspace"></div>
    <p class="copy light abs" style="left:12px;top:28px;width:80px;text-align:justify">Lorem ipsum dolor sit amet, quem prompta forensibus ei has, has saepe eloquentiam at. Enim consulatu percipitur ut nec, est fugit iudicabit te, alia consulatu an ius.</p>
    <p class="copy light abs" style="left:12px;top:90px;width:80px;text-align:justify">Lorem ipsum dolor sit amet, quem prompta forensibus ei has, has saepe eloquentiam at. Enim consulatu percipitur ut nec, est fugit iudicabit te, alia consulatu an ius.</p>
    <h2 class="heading abs" style="right:16px;top:14px">Data Slide</h2>
    <div class="rule" style="left:207px;top:28px;width:36px"></div>
    <p class="copy right abs" style="left:112px;top:34px;width:131px">Lorem ipsum dolor sit amet, quem prompta forensibus ei has, has saepe eloquentiam at. Enim consulatu percipitur ut nec, est fugit iudicabit te, alia consulatu an ius.</p>
    <svg class="abs" style="left:0;top:0" width="259" height="145" role="img" aria-label="Bar chart with three series across four categories">
      <text x="171" y="66" class="chart-title" font-size="3px">CHART TITLE</text>
      <g fill="#0f1d36">
        <rect x="127" y="84" width="3" height="44"/><rect x="158" y="92" width="3" height="36"/><rect x="189" y="88" width="3" height="40"/><rect x="220" y="80" width="3" height="48"/>
      </g>
      <g fill="#9fb4cc">
        <rect x="131" y="104" width="3" height="24"/><rect x="162" y="78" width="3" height="50"/><rect x="193" y="106" width="3" height="22"/><rect x="224" y="96" width="3" height="32"/>
      </g>
      <g fill="#5aa6d6">
        <rect x="135" y="96" width="3" height="32"/><rect x="166" y="100" width="3" height="28"/><rect x="197" y="90" width="3" height="38"/><rect x="228" y="74" width="3" height="54"/>
      </g>
      <line x1="122" y1="128" x2="240" y2="128" stroke="#ccd" stroke-width=".3"/>
      <g font-size="2.4" fill="#888" font-family="Lato, sans-serif"><text x="123" y="134">CATEGORY 1</text><text x="154" y="134">CATEGORY 2</text><text x="185" y="134">CATEGORY 3</text><text x="216" y="134">CATEGORY 4</text></g>
    </svg>
  </section>

  <!-- Data slide: single pie -->
  <section class="slide data-pie" style="left:311px;top:1032px">
    <svg class="facets" aria-hidden="true"><use href="#facet-bg"/></svg>
    <svg class="corner tr" aria-hidden="true"><use href="#corner-shape"/></svg>
    <h2 class="heading abs" style="left:18px;top:16px">Data Slide</h2>
    <div class="rule" style="left:18px;top:30px;width:36px"></div>
    <p class="copy abs" style="left:18px;top:36px;width:176px">Lorem ipsum dolor sit amet, quem prompta forensibus ei has, has saepe eloquentiam at. Enim consulatu percipitur ut nec, est fugit iudicabit te, alia consulatu an ius.</p>
    <p class="copy abs" style="left:18px;top:68px;width:120px">Lorem ipsum dolor sit amet, quem prompta forensibus ei has, has saepe eloquentiam at. Enim consulatu percipitur ut nec, est fugit iudicabit te, alia consulatu an ius.</p>
    <p class="copy abs" style="left:18px;top:106px;width:120px">Lorem ipsum dolor sit amet, quem prompta forensibus ei has, has saepe eloquentiam at. Enim consulatu percipitur ut nec, est fugit iudicabit te, alia consulatu an ius.</p>
    <svg class="abs" style="left:0;top:0" width="259" height="145" role="img" aria-label="Pie chart of sales by quarter">
      <text x="202" y="54" class="chart-title" font-size="3px">SALES</text>
      <use href="#pie" x="166" y="58" width="70" height="70"/>
      <g font-size="2.6" fill="#777" font-family="Lato, sans-serif">
        <circle cx="174" cy="134" r="1" fill="#6fa3c7"/><text x="176" y="135">1st Qtr</text>
        <circle cx="187" cy="134" r="1" fill="#0f1d36"/><text x="189" y="135">2nd Qtr</text>
        <circle cx="201" cy="134" r="1" fill="#16305a"/><text x="203" y="135">3rd Qtr</text>
        <circle cx="214" cy="134" r="1" fill="#5aa6d6"/><text x="216" y="135">4th Qtr</text>
      </g>
    </svg>
  </section>

  <!-- Thank you -->
  <section class="slide thank-you" style="left:578px;top:1032px">
    <div class="photo" style="left:0;top:0;width:142px;height:145px;background:linear-gradient(150deg,#1d6d85 0%,#2a7f96 45%,#8fb0bc 80%,#c9d6dc 100%)" role="img" aria-label="Teal-toned photo looking up at a glass office building"></div>
    <h2 class="heading abs" style="left:15px;top:22px;font-size:12px;color:var(--white)">Thank You</h2>
    <div class="abs" style="left:142px;top:0;width:117px;height:145px;background:var(--ink)"></div>
    <div class="abs" style="left:150px;top:72px;width:104px;display:flex;align-items:center;gap:4px">
      <span class="brand-mark" style="width:9px;height:9px;background:var(--white)"></span>
      <p class="brand" style="font-size:5.6px;color:var(--white);text-align:left">Keystone Ridge<br>Financial LLC.</p>
    </div>
    <p class="copy right light abs" style="left:150px;top:108px;width:100px"><b style="color:var(--white)">Insert contact person here</b><br>Lorem ipsum dolor sit amet, quem prompta forensibus ei has, has saepe eloquentiam at. Enim consulatu percipitur ut nec.</p>
  </section>

</main>
</body>
</html>
```